Vintage soap dispenser label

I'm making a series of glass bottle soap dispensers (soap, lotion, shampoo, etc.). I really love a competitor's design, but I don't want to copy it. I'm interested in the clean, urban vintage style. There can be a lot of filler text as in their design which fills the negative space, but note that the buyer will fill the bottles with their own products, so things like "100% Natural Ingredients" and the like are somewhat bogus. Because they are to be refillable, reusable bottles, some text to that effect may be more appropriate, plus our company name "Velmora Home", and perhaps the style of the bottle "Boston Round" and other text like the size of the bottle. I need a basic design, 3.25" wide x 3.5" tall and I will adjust the text as necessary for the various products my buyers will use. My competitor that is very similar to my business is https://shoplink.example/7KpR2vX. As you can see, they have a signature style. I'd like my own signature style. (I plan to have a vintage line and a contemporary line of products, so I'll likely be posting a second request for that.)

Requirements
Should not have
• Not too ornate. Should be somewhat minimalistic

```html
<!DOCTYPE html>
<html lang="en">
<head>
<meta charset="utf-8">
<title>Velmora Home – Shampoo Label</title>
<link rel="stylesheet" href="https://fonts.googleapis.com/css2?family=Oswald:wght@400&family=Jost:wght@400&display=swap">
<style>
  :root {
    --backdrop: #e7e7e7;
    --label-black: #000000;
    --ink-white: #ffffff;
    --ink-grey: #9a9a9a;
  }
  html, body {
    margin: 0;
    padding: 0;
    width: 1200px;
    height: 1000px;
    overflow: hidden;
    background: var(--backdrop);
  }
  .canvas {
    position: relative;
    width: 1200px;
    height: 1000px;
  }
  .label {
    position: absolute;
    left: 345px;
    top: 225px;
    width: 510px;
    height: 550px;
    background: var(--label-black);
  }
  .label-lines {
    position: absolute;
    left: 0;
    top: 0;
  }
  .label-text {
    position: absolute;
    left: 0;
    width: 510px;
    margin: 0;
    text-align: center;
    color: var(--ink-white);
    line-height: 1;
    white-space: nowrap;
  }
  .brand-name {
    top: 160px;
    font-family: "Oswald", sans-serif;
    font-size: 31px;
    letter-spacing: 0.5px;
  }
  .product-name {
    top: 228px;
    font-family: "Jost", sans-serif;
    font-size: 58px;
    letter-spacing: 6px;
    padding-left: 6px;
    box-sizing: border-box;
  }
  .product-tagline {
    top: 343px;
    font-family: "Oswald", sans-serif;
    font-size: 16px;
    letter-spacing: 1.6px;
    color: var(--ink-grey);
  }
  .product-claim {
    top: 423px;
    font-family: "Jost", sans-serif;
    font-size: 15px;
    letter-spacing: 3px;
  }
  .product-volume {
    top: 476px;
    font-family: "Oswald", sans-serif;
    font-size: 22px;
    letter-spacing: 2px;
  }
</style>
</head>
<body>
<main class="canvas">
  <section class="label" aria-label="Velmora Home shampoo bottle label">
    <svg class="label-lines" width="510" height="550" viewBox="0 0 510 550" aria-hidden="true">
      <g fill="none" stroke="var(--ink-white)" stroke-width="2">
        <rect class="frame-outer" x="21" y="22" width="468" height="506"/>
        <rect class="frame-inner" x="29" y="30" width="452" height="490"/>
        <line class="volume-divider" x1="29" y1="453" x2="481" y2="453"/>
        <circle class="brand-dot" cx="255" cy="105" r="36"/>
        <line class="ribbon-rule" x1="157" y1="335" x2="352" y2="335"/>
        <line class="ribbon-rule" x1="157" y1="370" x2="352" y2="370"/>
      </g>
      <g fill="var(--ink-grey)">
        <polygon class="ribbon-point" points="233,334 255,315 277,334"/>
        <polygon class="ribbon-point" points="233,371 255,390 277,371"/>
      </g>
    </svg>
    <p class="label-text brand-name">VELMORA HOME</p>
    <h1 class="label-text product-name" style="font-weight:400">SHAMPOO</h1>
    <p class="label-text product-tagline">ORIGINAL APOTHECARY</p>
    <p class="label-text product-claim">100% NATURAL INGREDIENTS</p>
    <p class="label-text product-volume">300ML</p>
  </section>
</main>
</body>
</html>
```